Norvane Staffing - White Collar Engineering Consultancy

I'm chasing a website to provide high level information about what Norvane Staffing is and service's we provide - only chasing something simple. We are a new white collar secondment/contractor/professional services/consultancy specialising is providing the best consultants into contractor roles.

Our primary industries are energy, gas, pipelines, water processing, power, projects, geographic information systems, design, accounting.

Our people are mechanical,/electrical/civil/process/chemical engineers, project engineers, project managers, technical experts, GIS analysts, integrity engineers, pipeline engineers,

Currently I have this domain registered through Zentrio - https://www.norvanestaffing-example.com/

I'd like to keep this domain but completely overhaul the website to be sleek and follow the logo styling.

Example websites within my industry that I like:
- https://www.brelwickworks-example.com.au/
- https://quarn-example.com.au/
- https://www.hdmtech-example.com.au/

I'd like the winner to code and assist with making the website functional under my domain.

Would like to include:
- industries
- services
- why work with us
- terms and conditions as per attached
- location (Brisbane)
- contact us form, that submits an email to sam.burow@norvanestaffing-example.com
- WorkLinker link

Would definitely be looking to polish the winning result with the designer over the phone or via email.

I will also add some infrastructure photos for use; otherwise please use generic CSG related infrastructure.

Cheers,

Sam

Industry/Entity Type

Energy, resources, gas, mining, geographic information systems, accounting, construction.

Coding

Coded - Design and coding required

Number of Pages Required

4 page

Colors
0054AA
0677BA
7BADD7
CADEEF
E8F1F8

Requirements
Must have
• Refer to project description

```html
<!DOCTYPE html>
<html lang="en">
<head>
<meta charset="utf-8">
<title>Norvane Staffing - White Collar Engineering Consultancy</title>
<link rel="stylesheet" href="https://fonts.googleapis.com/css2?family=Inter:wght@300;400;500;600;700&display=swap">
<style>
:root{
  --navy-deep:#11163d;
  --navy:#1d2250;
  --paper:#eff0eb;
  --board:#e9e9e9;
  --white:#ffffff;
  --soft:#f4f4f6;
  --ink:#1d2250;
  --muted:#6b6e82;
  --line:#d9dae2;
}
*{box-sizing:border-box;margin:0;padding:0}
html,body{width:1200px;height:2698px;overflow:hidden}
body{background:var(--board);font-family:"Inter",Arial,sans-serif;color:var(--ink);position:relative}
.abs{position:absolute}

/* style guide header */
.brand{display:flex;align-items:center;gap:8px;font-weight:700;color:var(--navy);white-space:nowrap}
.brand-dot{width:30px;height:30px;border-radius:50%;background:var(--navy)}
.guide-brand{left:203px;top:136px;font-size:22px}
.guide-title{font-size:25px;font-weight:400;color:#222}
.guide-font{left:595px;top:142px;font-size:17px;color:#777;font-weight:300}
.swatch{width:42px;height:42px;border-radius:50%;top:138px}
.swatch-label{font-size:9px;color:#555;top:187px}

/* site */
.site{left:222px;top:279px;width:792px;height:2318px;background:var(--white);overflow:hidden}
.topbar{left:22px;top:0;width:748px;height:25px;border:1px solid var(--line);border-top:0;display:flex;font-size:6px;color:#333;white-space:nowrap}
.topbar span{display:flex;align-items:center;padding:0 10px;border-right:1px solid var(--line)}
.topbar .grow{flex:1}
.topbar span:last-child{border-right:0}
.nav{left:22px;top:34px;width:748px;height:26px;display:flex;align-items:center}
.nav .brand{font-size:13px}
.nav .brand-dot{width:18px;height:18px}
.nav-links{display:flex;gap:34px;font-size:7.5px;color:#333;margin-left:102px}
.btn-contact{margin-left:auto;background:var(--navy);color:var(--white);font-size:7px;font-weight:600;padding:9px 16px}

.hero{left:22px;top:69px;width:748px;height:385px;background:linear-gradient(180deg,#bdbdbd 0%,#9a9a9a 45%,#5c5c5c 100%)}
.hero h1{left:40px;top:36px;font-size:30px;line-height:32px;font-weight:600;color:var(--navy);width:380px}
.hero h1 em{font-style:normal;color:var(--white)}
.hero p{left:55px;top:144px;width:320px;font-size:9.5px;line-height:14px;color:var(--white);border-left:1px solid var(--white);padding-left:2px}

.h2{font-size:23px;font-weight:500;color:var(--navy);white-space:nowrap}
.eyebrow{font-size:6.5px;letter-spacing:2px;color:#888;text-transform:uppercase}
.body{font-size:7.5px;line-height:12.5px;color:#555}

.about-title{left:22px;top:504px}
.about-photo{left:22px;top:555px;width:160px;height:106px;background:linear-gradient(135deg,#c9c9c9,#5e5e5e)}
.about-lead{left:318px;top:507px;width:190px;font-size:9.5px;line-height:14px;font-weight:600;color:#222}
.about-copy{left:318px;top:561px;width:190px}
.stat{left:697px;font-size:38px;font-weight:300;color:var(--navy)}
.stat-label{left:697px;font-size:7.5px;color:#444}

.services{left:22px;top:726px;width:748px;height:287px;background:var(--soft)}
.svc{width:130px}
.svc h3{font-size:13px;font-weight:500;color:var(--navy);margin-bottom:6px;white-space:nowrap}
.svc-icon{width:38px;height:38px}

.ind-arrow{width:22px;height:22px;border-radius:50%;display:flex;align-items:center;justify-content:center}
.card{top:1130px;width:198px;height:112px}
.card-photo{position:absolute;inset:0;background:linear-gradient(160deg,#bcbcbc,#5a5a5a)}
.card-label{position:absolute;left:0;bottom:0;width:115px;height:35px;background:var(--white);display:flex;align-items:center;justify-content:space-between;padding:0 10px;font-size:8px;color:var(--navy);white-space:nowrap}

.values-band{left:0;top:1296px;width:792px;height:362px;background:var(--soft)}
.values-list{left:318px;top:1351px;width:452px;height:252px;background:var(--white);padding:20px 38px}
.values-list li{list-style:none;display:flex;justify-content:space-between;font-size:7.5px;color:var(--navy);border-bottom:1px solid var(--line);padding:13px 0 10px}
.values-list li:last-child{border-bottom:0}
.feat{font-size:7px;color:#444;display:flex;align-items:center;gap:5px;white-space:nowrap}

.video{left:0;top:1658px;width:792px;height:346px;background:linear-gradient(180deg,#d8d8d8 0%,#b3b3b3 40%,#8a8a8a 100%)}
.play{left:32px;top:227px;width:60px;height:60px;border-radius:50%;background:var(--white);display:flex;align-items:center;justify-content:center}

.footer{left:0;top:2004px;width:792px;height:314px;background:var(--navy);color:var(--white)}
.footer .brand{color:var(--white);font-size:13px}
.footer .brand-dot{width:18px;height:18px;background:var(--white)}
.fcol h4{font-size:7px;font-weight:400;color:#9aa0c6;margin-bottom:10px;white-space:nowrap}
.fcol a{display:block;font-size:7px;color:var(--white);text-decoration:none;margin-bottom:6px;white-space:nowrap}
.newsletter{left:462px;top:181px;width:313px;height:30px;background:#262c5e;display:flex;align-items:center;padding-left:13px;font-size:7px}
.newsletter-btn{position:absolute;right:0;top:0;width:30px;height:30px;background:var(--white);display:flex;align-items:center;justify-content:center}
.f-deco{left:-30px;top:60px;width:230px;height:230px;border-radius:50%;background:#232a5c}
.fine{font-size:5.5px;color:#c9cce4;white-space:nowrap}
</style>
</head>
<body>

<div class="abs brand guide-brand"><span class="brand-dot"></span>Norvane Staffing</div>
<div class="abs guide-title" style="left:595px;top:100px">Fonts:</div>
<div class="abs guide-font">Neue Haas Unica</div>
<div class="abs guide-title" style="left:888px;top:100px">Colors:</div>
<div class="abs swatch" style="left:890px;background:#11163d"></div>
<div class="abs swatch" style="left:941px;background:#1d2250"></div>
<div class="abs swatch" style="left:993px;background:#eff0eb;border:1px solid #ddd"></div>
<div class="abs swatch-label" style="left:894px">#11163d</div>
<div class="abs swatch-label" style="left:944px">#1d2250</div>
<div class="abs swatch-label" style="left:996px">#eff0eb</div>

<main class="abs site">
  <div class="abs topbar">
    <span style="width:150px">sam.burow@norvanestaffing-example.com</span>
    <span class="grow"></span>
    <span style="width:200px;justify-content:center">Level 9/42 Kestrel Lane, Brisbane City QLD 4000, Australia</span>
    <span class="grow"></span>
    <span>Follow Us: <b style="color:var(--navy);margin-left:10px">WorkLinker</b></span>
  </div>

  <nav class="abs nav">
    <div class="brand"><span class="brand-dot"></span>Norvane Staffing</div>
    <div class="nav-links"><span>Home</span><span>About Us</span><span>Industries</span><span>Services</span><span>Why Work With Us</span></div>
    <span class="btn-contact">Contact Us</span>
  </nav>

  <section class="abs hero" role="img" aria-label="Black and white photo of gas pipeline valves and infrastructure under a cloudy sky">
    <h1 class="abs">Pioneering <em>White Collar</em> Engineering Consulting and Solutions</h1>
    <p class="abs">Discover our trailblazing white-collar engineering solutions, where the innovation, expertise, and dedication meet the excellence in addressing complex modern industry challenges head-on.</p>
  </section>

  <h2 class="abs h2 about-title">About Us</h2>
  <div class="abs about-photo" role="img" aria-label="Excavator working on a construction site"></div>
  <p class="abs about-lead">We stand as a premier firm specializing in secondment, contractor placement, professional services, and consultancy.</p>
  <div class="abs about-copy body">
    <p>At Norvane Staffing, we believe that the right people can make all the difference in the success of a project or an organization. We take pride in being the link that connects talented professionals with opportunities where they can thrive.</p>
    <p style="margin-top:12px">Our commitment to excellence drives our mission of linking the top-tier consultants with contractor positions spanning diverse industries.</p>
  </div>
  <div class="abs stat" style="top:500px">13+</div>
  <div class="abs stat-label" style="top:546px">Years of Experience</div>
  <div class="abs stat" style="top:576px">504</div>
  <div class="abs stat-label" style="top:623px">Completed Projects</div>

  <section class="abs services">
    <div class="abs eyebrow" style="left:37px;top:56px">Our Services</div>
    <h2 class="abs h2" style="left:37px;top:66px">What We Do</h2>

    <svg class="abs svc-icon" style="left:287px;top:55px" viewBox="0 0 40 40" fill="none" stroke="#9a9cae" stroke-width="2"><path d="M20 3 35 11v18L20 37 5 29V11z"/><path d="M20 10 28 15v10l-8 5-8-5V15z"/></svg>
    <div class="abs svc" style="left:332px;top:52px"><h3>Planning</h3><p class="body">We help you chart a clear path forward by setting objectives, resource allocation, and outlining actionable steps.</p></div>

    <svg class="abs svc-icon" style="left:538px;top:55px" viewBox="0 0 40 40" fill="none" stroke="#9a9cae" stroke-width="2"><path d="M32 8A16 16 0 1 0 32 32"/><path d="M27 13A9 9 0 1 0 27 27"/></svg>
    <div class="abs svc" style="left:582px;top:52px"><h3>Advisory</h3><p class="body">We offer insightful guidance and tailored recommendations to help you navigate challenges and seize opportunities.</p></div>

    <svg class="abs svc-icon" style="left:287px;top:166px" viewBox="0 0 40 40" fill="none" stroke="#9a9cae" stroke-width="2"><path d="M20 4 37 35H3z"/><path d="M20 14 29 30H11z"/></svg>
    <div class="abs svc" style="left:332px;top:163px"><h3>Project Management</h3><p class="body">We bring efficiency, structure, and accountability to every endeavor, so you can focus on your project's success and more.</p></div>

    <svg class="abs svc-icon" style="left:538px;top:166px" viewBox="0 0 40 40" fill="none" stroke="#9a9cae" stroke-width="2"><path d="M3 12h34L12 30h25"/></svg>
    <div class="abs svc" style="left:582px;top:163px"><h3>Design</h3><p class="body">We transform your vision into compelling &amp; user-friendly solutions that stand out in today's competitive landscape.</p></div>
  </section>

  <div class="abs eyebrow" style="left:22px;top:1065px">Who We Work With</div>
  <h2 class="abs h2" style="left:22px;top:1075px">Industries We Serve</h2>
  <div class="abs ind-arrow" style="left:718px;top:1085px;background:#e4e4e8"><svg width="10" height="10" viewBox="0 0 10 10" fill="none" stroke="#333"><path d="M9 5H1M4 2 1 5l3 3"/></svg></div>
  <div class="abs ind-arrow" style="left:746px;top:1085px;background:var(--navy)"><svg width="10" height="10" viewBox="0 0 10 10" fill="none" stroke="#fff"><path d="M1 5h8M6 2l3 3-3 3"/></svg></div>

  <div class="abs card" style="left:-188px"><div class="card-photo" role="img" aria-label="Industrial site photo"></div></div>
  <div class="abs card" style="left:22px"><div class="card-photo" role="img" aria-label="Oil and gas processing plant"></div><div class="card-label">Oil &amp; Gas <span>→</span></div></div>
  <div class="abs card" style="left:233px"><div class="card-photo" role="img" aria-label="Water processing pipeline at sunset"></div><div class="card-label">Water Process. <span>→</span></div></div>
  <div class="abs card" style="left:443px"><div class="card-photo" role="img" aria-label="Aerial view of power and energy facility"></div><div class="card-label">Power / Energy <span>→</span></div></div>
  <div class="abs card" style="left:653px"><div class="card-photo" role="img" aria-label="Pipeline valves and infrastructure"></div><div class="card-label">Pipelines <span>→</span></div></div>

  <section class="abs values-band">
    <div class="abs eyebrow" style="left:22px;top:56px">Why Choose Us</div>
    <h2 class="abs h2" style="left:22px;top:66px">Core Values</h2>
    <p class="abs body" style="left:22px;top:109px;width:225px">Our commitment to excellence is grounded in a set of core values that guide our actions and define our identity. These values shape our interactions with clients, ensuring that we provide the highest level of service.</p>
    <div class="abs feat" style="left:22px;top:177px"><svg width="10" height="10" viewBox="0 0 10 10" fill="none" stroke="#555"><circle cx="5" cy="5" r="4"/><path d="m3 5 1.5 1.5L7 3.5"/></svg>Feature Goes Here</div>
    <div class="abs feat" style="left:123px;top:177px"><svg width="10" height="10" viewBox="0 0 10 10" fill="none" stroke="#555"><circle cx="5" cy="5" r="4"/><path d="m3 5 1.5 1.5L7 3.5"/></svg>Feature Goes Here</div>
    <div class="abs feat" style="left:22px;top:197px"><svg width="10" height="10" viewBox="0 0 10 10" fill="none" stroke="#555"><circle cx="5" cy="5" r="4"/><path d="m3 5 1.5 1.5L7 3.5"/></svg>Feature Goes Here</div>
    <div class="abs feat" style="left:123px;top:197px"><svg width="10" height="10" viewBox="0 0 10 10" fill="none" stroke="#555"><circle cx="5" cy="5" r="4"/><path d="m3 5 1.5 1.5L7 3.5"/></svg>Feature Goes Here</div>
  </section>
  <ul class="abs values-list">
    <li>Client-Centric Approach<span>+</span></li>
    <li>Diversity and Inclusion<span>+</span></li>
    <li>Collaboration<span>+</span></li>
    <li>Innovation<span>+</span></li>
    <li>Integrity<span>+</span></li>
    <li>Adaptability<span>+</span></li>
  </ul>

  <section class="abs video" role="img" aria-label="Field engineer in hi-vis walking through a grassy paddock beside a fence line">
    <div class="abs eyebrow" style="left:22px;top:143px;color:#555">The Process</div>
    <h2 class="abs h2" style="left:22px;top:153px;line-height:27px">A Deeper Dive into<br>How We Operate</h2>
    <div class="abs play"><svg width="14" height="14" viewBox="0 0 14 14"><path d="M3 1v12l10-6z" fill="#1d2250"/></svg></div>
  </section>

  <footer class="abs footer">
    <div class="abs f-deco"></div>
    <div class="abs brand" style="left:22px;top:48px"><span class="brand-dot"></span>Norvane Staffing</div>
    <div class="abs fcol" style="left:376px;top:48px"><h4>Company</h4><a>About</a><a>Why Choose Us</a></div>
    <div class="abs fcol" style="left:464px;top:48px"><h4>Industries</h4><a>Oil and Gas</a><a>Pipelines</a><a>Water Processing</a><a>Energy and Power</a><a>GIS</a></div>
    <div class="abs fcol" style="left:560px;top:48px"><h4>Services</h4><a>Engineering</a><a>Planning</a><a>Civil Engineering</a><a>Audit &amp; Inspection</a></div>
    <div class="abs fcol" style="left:652px;top:48px"><h4>Get in Touch</h4><a style="font-size:5.8px">sam.burow@norvanestaffing-example.com</a><a>Brisbane</a></div>
    <div class="abs fcol" style="left:462px;top:167px"><h4>Subscribe to Newsletter</h4></div>
    <div class="abs newsletter">Enter Your Email Address
      <span class="newsletter-btn"><svg width="12" height="12" viewBox="0 0 12 12" fill="none" stroke="#1d2250"><path d="M1 6 11 1 8 11 6 7z"/></svg></span>
    </div>
    <div class="abs fine" style="left:22px;top:264px">© 2023 Norvane Staffing - All rights reserved</div>
    <div class="abs fine" style="left:462px;top:264px">Privacy Policy | Terms of Use</div>
    <div class="abs fine" style="left:735px;top:264px;color:#fff;font-weight:600">WorkLinker</div>
  </footer>
</main>
</body>
</html>
```